A5 Flyer for Financial Services Business

I am after a re-design of our business flyer to fit in with our new branding style and logo colour scheme. Wanting something with a bit of designer flair that I could not create myself. I have included the flyer which I created which lacks style so dazzle me.

I want to use the same content.

Text for main body of flyer is

Are you a small business owner, tradie or KTAV Service Provider struggling to stay on top of your bookkeeping and compliance obligations? If so we would love to help you get back on track and take control of your business finances so that you can make informed business decisions and focus on what you do best.

We have over 20 years industry experience and, as a small business ourselves, we are able to offer our clients a personal bookkeeping solution tailored to meet the needs of your business.

Accounts Payable | Accounts Receivable
Customer Invoicing
Bank and Credit Card Reconciliations
Payroll | Superannuation | Payroll Tax
Business Activity | Instalment Activity Statements
Regular Financial Reports
Ledgerly and Tallybook Set-Up and Training

```html
<!DOCTYPE html>
<html lang="en">
<head>
<meta charset="utf-8">
<title>Even Keel Financial Services – Bookkeeping Flyer</title>
<link rel="stylesheet" href="https://fonts.googleapis.com/css2?family=Poppins:wght@300;400;500;600;700;800&display=swap">
<style>
  :root{
    --navy:#0d3d55;
    --navy-deep:#0a3349;
    --teal:#13808b;
    --teal-dark:#0b5e6d;
    --teal-bright:#28b3be;
    --stage:#c9cbcd;
    --white:#ffffff;
    --ink:#1f2a30;
    --badge-fill:#d5dde0;
  }
  *{box-sizing:border-box;margin:0;padding:0}
  html,body{width:1200px;height:2230px;overflow:hidden;background:var(--stage);font-family:'Poppins',sans-serif}
  .flyer{position:absolute;left:50px;top:335px;width:914px;height:1296px;background:var(--white);
    transform:scale(1.2035);transform-origin:0 0;overflow:hidden;box-shadow:0 6px 24px rgba(0,0,0,.25)}
  .art{position:absolute;left:0;top:0}
  .brand{position:absolute;left:48px;top:50px;width:300px;text-align:center;color:#4a6f7d;font-weight:300}
  .brand-dot{display:block;width:78px;height:78px;border-radius:50%;background:var(--teal);margin:0 auto 10px}
  .brand-name{font-size:31px;letter-spacing:.5px;line-height:1}
  .brand-sub{font-size:15px;letter-spacing:8px;margin-top:4px}
  .headline{position:absolute;left:48px;top:234px;color:var(--white);font-weight:800;font-size:41px;line-height:45px;letter-spacing:.3px}
  .intro{position:absolute;left:48px;top:413px;width:560px}
  .intro-lead{color:var(--navy);font-weight:700;font-size:22.5px;line-height:29px;white-space:nowrap}
  .intro-body{color:var(--ink);font-size:21px;line-height:26px;margin-top:8px;padding-left:3px;white-space:nowrap}
  .experience{position:absolute;left:633px;top:356px;width:240px;color:var(--white)}
  .stars{color:#f2c230;font-size:26px;letter-spacing:4px;text-align:center;margin-left:-30px}
  .exp-over{font-size:22px;letter-spacing:2px;font-weight:400;margin-top:2px}
  .exp-row{display:flex;align-items:flex-start;margin-top:2px}
  .exp-num{font-size:86px;font-weight:700;line-height:76px;color:var(--teal-bright);letter-spacing:-6px;margin-right:6px}
  .exp-years{font-size:38px;font-weight:700;line-height:38px}
  .exp-industry{font-size:17px;letter-spacing:4px;line-height:20px}
  .exp-tag{display:inline-block;background:var(--teal-bright);font-weight:600;font-size:18px;padding:0 4px;line-height:22px;letter-spacing:.5px}
  .exp-text{font-size:16px;line-height:20px;margin-top:8px}
  .services{position:absolute;left:0;top:665px;width:914px;height:418px;background:linear-gradient(180deg,var(--teal) 0%,#127985 100%)}
  .divider{position:absolute;left:442px;top:30px;width:1px;height:365px;background:rgba(255,255,255,.35)}
  .service{position:absolute;display:flex;align-items:center;height:52px;color:var(--white);font-weight:600;font-size:22.5px;line-height:26px}
  .service svg{flex:none;margin-right:12px}
  .contact-tab{position:absolute;left:0;top:1103px;width:345px;height:42px;background:var(--navy);color:var(--white);
    font-weight:700;font-size:22px;line-height:42px;padding-left:56px;letter-spacing:.5px;border-radius:0 6px 6px 0;box-shadow:2px 3px 4px rgba(0,0,0,.25)}
  .contact-line{position:absolute;left:48px;display:flex;align-items:center;color:var(--ink)}
  .phone{top:1153px;font-size:32px;font-weight:700}
  .email{top:1195px;font-size:17px;font-weight:500}
  .web{top:1220px;font-size:17px;font-weight:500}
  .contact-line svg{margin-right:12px;flex:none}
  .badge{position:absolute;top:1127px;width:108px;height:113px;border:2px solid #c9ced2;border-radius:6px;background:var(--white);display:flex;align-items:center;justify-content:center}
  .badge-mark{width:62px;height:62px;border-radius:50%;background:var(--badge-fill)}
</style>
</head>
<body>
<main class="flyer">
  <svg class="art" width="914" height="1296" viewBox="0 0 914 1296">
    <defs>
      <linearGradient id="bandGrad" x1="0" y1="0" x2="1" y2="0">
        <stop offset="0" stop-color="#0d3d55"/>
        <stop offset="1" stop-color="#14858f"/>
      </linearGradient>
      <linearGradient id="triGrad" x1="0" y1="0" x2="0" y2="1">
        <stop offset="0" stop-color="#0b5e6d"/>
        <stop offset="1" stop-color="#17959f"/>
      </linearGradient>
      <linearGradient id="photoGrad" x1="0" y1="0" x2="1" y2="1">
        <stop offset="0" stop-color="#e9e6e4"/>
        <stop offset=".55" stop-color="#b59a84"/>
        <stop offset="1" stop-color="#2d3440"/>
      </linearGradient>
      <linearGradient id="silver" x1="0" y1="0" x2="0" y2="1">
        <stop offset="0" stop-color="#d7dadd"/>
        <stop offset="1" stop-color="#7d848a"/>
      </linearGradient>
    </defs>
    <polygon points="380,0 560,0 470,130" fill="url(#triGrad)"/>
    <polygon points="560,0 914,0 914,385 590,385 472,148" fill="url(#photoGrad)" role="img" aria-label="Photo of a bookkeeper in a navy blazer working on paperwork at a desk with a calculator"/>
    <polygon points="445,150 468,145 590,385 570,385" fill="url(#silver)"/>
    <polygon points="0,212 470,212 570,388 0,388" fill="url(#bandGrad)"/>
    <polygon points="595,380 740,315 885,380 885,665 595,665" fill="var(--navy-deep)" stroke="#1b7f8c" stroke-width="6"/>
  </svg>

  <div class="brand">
    <span class="brand-dot"></span>
    <div class="brand-name">EVEN KEEL</div>
    <div class="brand-sub">Financial Services</div>
  </div>

  <h1 class="headline">BOOKKEEPING<br>TAILORED TO YOUR<br>BUSINESS NEEDS</h1>

  <section class="intro">
    <p class="intro-lead">Are you a small business owner, tradie or<br>KTAV Service Provider struggling to stay<br>on top of your bookkeeping and<br>compliance obligations?</p>
    <p class="intro-body">If so we would love to help you get back on<br>track and take control of your business finances<br>so that you can make informed business<br>decisions and focus on what you do best.</p>
  </section>

  <aside class="experience">
    <div class="stars">★★★</div>
    <div class="exp-over">WE HAVE OVER</div>
    <div class="exp-row">
      <div class="exp-num">20</div>
      <div>
        <div class="exp-years">YEARS</div>
        <div class="exp-industry">INDUSTRY</div>
        <div class="exp-tag">EXPERIENCE</div>
      </div>
    </div>
    <p class="exp-text">And, as a small business ourselves, we are able to offer our clients a <strong>personal bookkeeping solution</strong> tailored to meet the needs of your business.</p>
  </aside>

  <section class="services">
    <div class="divider"></div>
    <div class="service" style="left:50px;top:23px"><svg width="52" height="52" viewBox="0 0 52 52"><circle cx="26" cy="26" r="24" fill="none" stroke="#fff" stroke-width="2" stroke-dasharray="3 2"/><circle cx="26" cy="26" r="18" fill="#fff"/><rect x="18" y="20" width="16" height="12" rx="2" fill="none" stroke="var(--teal)" stroke-width="2"/></svg>Accounts Payable</div>
    <div class="service" style="left:50px;top:89px"><svg width="52" height="52" viewBox="0 0 52 52"><circle cx="26" cy="26" r="24" fill="none" stroke="#fff" stroke-width="2" stroke-dasharray="3 2"/><circle cx="26" cy="26" r="18" fill="#fff"/><rect x="19" y="17" width="13" height="18" rx="1" fill="none" stroke="var(--teal)" stroke-width="2"/></svg>Accounts Receivable</div>
    <div class="service" style="left:50px;top:152px"><svg width="52" height="52" viewBox="0 0 52 52"><circle cx="26" cy="26" r="24" fill="none" stroke="#fff" stroke-width="2" stroke-dasharray="3 2"/><circle cx="26" cy="26" r="18" fill="#fff"/><path d="M19 18h14M19 24h14M19 30h9" stroke="var(--teal)" stroke-width="2"/></svg>Customer Invoicing</div>
    <div class="service" style="left:50px;top:221px"><svg width="52" height="52" viewBox="0 0 52 52"><circle cx="26" cy="26" r="24" fill="none" stroke="#fff" stroke-width="2" stroke-dasharray="3 2"/><circle cx="26" cy="26" r="18" fill="#fff"/><rect x="16" y="20" width="20" height="13" rx="2" fill="none" stroke="var(--teal)" stroke-width="2"/><path d="M16 25h20" stroke="var(--teal)" stroke-width="2"/></svg>Bank and Credit Card<br>Reconciliations</div>
    <div class="service" style="left:50px;top:282px"><svg width="52" height="52" viewBox="0 0 52 52"><circle cx="26" cy="26" r="24" fill="none" stroke="#fff" stroke-width="2" stroke-dasharray="3 2"/><circle cx="26" cy="26" r="18" fill="#fff"/><circle cx="26" cy="27" r="8" fill="none" stroke="var(--teal)" stroke-width="2"/></svg>Payroll</div>
    <div class="service" style="left:50px;top:345px"><svg width="52" height="52" viewBox="0 0 52 52"><circle cx="26" cy="26" r="24" fill="none" stroke="#fff" stroke-width="2" stroke-dasharray="3 2"/><circle cx="26" cy="26" r="18" fill="#fff"/><path d="M18 33V25M24 33V21M30 33V23M36 33V18" stroke="var(--teal)" stroke-width="2"/></svg>Superannuation</div>

    <div class="service" style="left:487px;top:22px"><svg width="52" height="52" viewBox="0 0 52 52"><circle cx="26" cy="26" r="24" fill="none" stroke="#fff" stroke-width="2" stroke-dasharray="3 2"/><circle cx="26" cy="26" r="18" fill="#fff"/><rect x="19" y="17" width="14" height="18" rx="1" fill="none" stroke="var(--teal)" stroke-width="2"/><path d="M22 23h8M22 28h8" stroke="var(--teal)" stroke-width="2"/></svg>Payroll Tax</div>
    <div class="service" style="left:487px;top:87px"><svg width="52" height="52" viewBox="0 0 52 52"><circle cx="26" cy="26" r="24" fill="none" stroke="#fff" stroke-width="2" stroke-dasharray="3 2"/><circle cx="26" cy="26" r="18" fill="#fff"/><rect x="17" y="21" width="18" height="13" rx="2" fill="none" stroke="var(--teal)" stroke-width="2"/><path d="M22 21v-3h8v3" fill="none" stroke="var(--teal)" stroke-width="2"/></svg>Business Activity</div>
    <div class="service" style="left:487px;top:152px"><svg width="52" height="52" viewBox="0 0 52 52"><circle cx="26" cy="26" r="24" fill="none" stroke="#fff" stroke-width="2" stroke-dasharray="3 2"/><circle cx="26" cy="26" r="18" fill="#fff"/><path d="M18 33l6-7 5 4 7-10" fill="none" stroke="var(--teal)" stroke-width="2"/></svg>Regular Financial Reports</div>
    <div class="service" style="left:487px;top:219px"><svg width="52" height="52" viewBox="0 0 52 52"><circle cx="26" cy="26" r="24" fill="none" stroke="#fff" stroke-width="2" stroke-dasharray="3 2"/><circle cx="26" cy="26" r="18" fill="#fff"/><rect x="19" y="17" width="14" height="18" rx="1" fill="none" stroke="var(--teal)" stroke-width="2"/><path d="M22 22h8M22 26h8M22 30h8" stroke="var(--teal)" stroke-width="1.5"/></svg>Instalment Activity<br>Statements</div>
    <div class="service" style="left:487px;top:291px"><svg width="52" height="52" viewBox="0 0 52 52"><circle cx="26" cy="26" r="24" fill="none" stroke="#fff" stroke-width="2" stroke-dasharray="3 2"/><circle cx="26" cy="26" r="18" fill="#fff"/><rect x="22" y="18" width="15" height="11" rx="1" fill="none" stroke="var(--teal)" stroke-width="2"/><circle cx="18" cy="24" r="3" fill="var(--teal)"/><path d="M14 35c0-5 8-5 8 0" fill="var(--teal)"/></svg>Ledgerly and Tallybook<br>Set-Up and Training</div>
  </section>

  <div class="contact-tab">CONTACT US TODAY</div>
  <div class="contact-line phone"><svg width="24" height="24" viewBox="0 0 24 24"><path d="M6 2l4 4-2 3c1 3 4 6 7 7l3-2 4 4-3 4C10 21 3 14 2 5z" fill="var(--teal)"/></svg>0400 123 987</div>
  <div class="contact-line email"><svg width="20" height="14" viewBox="0 0 20 14"><rect width="20" height="14" fill="var(--navy)"/><path d="M0 0l10 8 10-8" fill="none" stroke="#fff" stroke-width="1.5"/></svg>hello@evenkeelfinancial.com.au</div>
  <div class="contact-line web"><svg width="20" height="20" viewBox="0 0 20 20"><circle cx="10" cy="10" r="9" fill="var(--teal)"/><path d="M1 10h18M10 1c-4 5-4 13 0 18M10 1c4 5 4 13 0 18" fill="none" stroke="#fff" stroke-width="1.2"/></svg>www.evenkeelfinancial.com.au</div>

  <div class="badge" style="left:523px" role="img" aria-label="Registered tax agent badge"><span class="badge-mark"></span></div>
  <div class="badge" style="left:637px" role="img" aria-label="Certified accounting software advisor badge"><span class="badge-mark"></span></div>
  <div class="badge" style="left:751px" role="img" aria-label="Certified cloud accounting advisor badge"><span class="badge-mark"></span></div>
</main>
</body>
</html>
```